Coinvale Landing Page | A free, personalized stock market email

We are looking for someone to revamp our landing page at https://coinvale-example.com . You should get to know the product and what it offers, and present new designs for our landing page. Feel free to use assets that currently exist on the page, as well as any new assets that you can put together. This landing page should make it obvious what the product does and aim to dramatically increase our conversion rate. We are looking for creativity, uniqueness, and clarity of purpose.

Target Market(s)

People who are invested in, or interested in being invested in, the stock market

Industry/Entity Type

Finance

Number of Pages Required

1 page

Font styles to use
Sans Serif

Requirements
Must have
• Creativity, sleek/minimal design, existing color palette and logos
Nice to have
• Effective copy
Should not have
• Clutter

```html
<!DOCTYPE html>
<html lang="en">
<head>
<meta charset="utf-8">
<title>Coinvale Landing Page — Desktop and Mobile</title>
<link href="https://fonts.googleapis.com/css2?family=Poppins:wght@300;400;500;600;700;800&display=swap" rel="stylesheet">
<style>
:root{
  --board:#ececec;
  --white:#ffffff;
  --blue:#0a7bd0;
  --blue-deep:#0668b8;
  --cyan:#2fe3ea;
  --sky:#d9f7fb;
  --ink:#262626;
  --footer:#3d3a3b;
  --badge-top:#1a74c2;
  --badge-bottom:#2c3139;
}
*{box-sizing:border-box;margin:0;padding:0}
html,body{width:1200px;height:2698px;overflow:hidden;background:var(--board);font-family:'Poppins',sans-serif;color:var(--ink)}
.board{position:relative;width:1200px;height:2698px}
.abs{position:absolute}
.board-label{position:absolute;top:20px;font-size:20px;font-weight:500;color:#111}

.page{position:absolute;background:var(--white);overflow:hidden}
.page--desktop{left:0;top:69px;width:857px;height:2083px}
.page--mobile{left:947px;top:69px;width:215px;height:2596px}
.page .abs{position:absolute}

.brand{font-weight:500;color:var(--blue);display:flex;align-items:center;gap:8px}
.brand-dot{border-radius:50%;background:var(--blue);display:inline-block}
.brand--light{color:var(--white)}
.brand--light .brand-dot{background:var(--white)}

.nav a{position:absolute;font-size:9px;color:#222;text-decoration:none}
.nav a.is-active{color:var(--blue)}
.social-dot{position:absolute;border-radius:50%}

.btn-signin{border:1.5px solid var(--blue);color:var(--blue);border-radius:14px;font-size:9px;display:flex;align-items:center;justify-content:center}
.btn-cta{background:var(--white);border-radius:20px;display:flex;align-items:center;justify-content:space-between;font-weight:600;color:#222;box-shadow:0 0 0 2px var(--blue) inset}
.btn-cta .arrow{background:var(--blue);border-radius:14px;display:flex;align-items:center;justify-content:center}

.hero-line{color:var(--white);line-height:1;letter-spacing:-0.5px}
.hero-line .thin{font-weight:300}
.hero-line .bold{font-weight:800}

.lede{font-weight:300;color:#333;white-space:nowrap}
.headline{font-weight:600;color:var(--blue);white-space:nowrap}
.body-copy{color:#333;line-height:1.45}

.art{position:absolute}
.art--network{border-radius:48% 52% 44% 56% / 52% 46% 54% 48%;background:radial-gradient(ellipse at 50% 62%,#a9c8bc 0%,#cfdcd6 30%,#e2e4e3 60%,#ebebeb 100%)}
.art--beach{background:linear-gradient(180deg,rgba(255,255,255,0) 0%,#bfe6f3 35%,#58c9ec 62%,var(--cyan) 100%)}
.art--photo{background:radial-gradient(ellipse at 45% 18%,#d9a184 0%,#b86a4d 14%,transparent 26%),radial-gradient(ellipse at 55% 60%,#e6e6e8 0%,#cfcfd3 18%,transparent 30%),linear-gradient(180deg,#6b3a24 0%,#c1272d 38%,#a51d24 100%)}
.art--sketch{background:linear-gradient(180deg,rgba(255,255,255,0.35),rgba(255,255,255,0.08))}
.art--field{background:linear-gradient(180deg,rgba(255,255,255,0) 0%,#c7ebf6 32%,#6fd3ee 64%,var(--cyan) 100%)}

.step{position:absolute;text-align:center}
.step-badge{position:relative;margin:0 auto;border-radius:50%;background:var(--sky)}
.step-badge span{position:absolute;left:50%;transform:translateX(-50%);border-radius:14px;background:linear-gradient(180deg,var(--badge-top),var(--badge-bottom));color:var(--white);font-weight:700;display:flex;align-items:center;justify-content:center}
.step-title{color:var(--blue);font-weight:500}
.step-copy{color:#444;line-height:1.45}

.footer{position:absolute;background:var(--footer);color:var(--white)}
.footer .tag .accent{color:var(--blue)}
.footer .sample{color:var(--cyan);position:absolute}
.footer h4{position:absolute;color:var(--cyan);font-weight:500}
.footer .links a{position:absolute;color:var(--white);text-decoration:none}
.footer .rule{position:absolute;height:1px;background:#5d5a5b}

.phone{position:absolute;border:3px solid #222;border-radius:12px;background:var(--white);overflow:hidden}
.phone .line{position:absolute;height:3px;background:#d5d8dc;border-radius:2px}
.phone .line.dark{background:#444}
.phone .toggle{position:absolute;width:8px;height:4px;border-radius:2px;background:#3ec46d}
</style>
</head>
<body>
<div class="board">
  <div class="board-label" style="left:40px">Desktop Version</div>
  <div class="board-label" style="left:947px">Mobile Version</div>

  <!-- DESKTOP -->
  <main class="page page--desktop">
    <svg class="abs" style="left:0;top:0" width="857" height="440" aria-hidden="true">
      <defs>
        <linearGradient id="heroFade" x1="0" y1="0" x2="0" y2="1">
          <stop offset="0" stop-color="#ffffff"/>
          <stop offset="0.22" stop-color="#e6f2fb"/>
          <stop offset="0.5" stop-color="#0a7bd0"/>
          <stop offset="1" stop-color="#0a7bd0"/>
        </linearGradient>
      </defs>
      <path d="M0 0 H857 V125 L60 360 Q20 372 0 350 Z" fill="url(#heroFade)"/>
    </svg>

    <div class="abs brand" style="left:40px;top:9px;font-size:26px"><span class="brand-dot" style="width:12px;height:12px"></span>Coinvale</div>
    <nav class="nav">
      <a class="is-active" style="left:318px;top:20px">Home</a>
      <a style="left:377px;top:20px">About</a>
      <a style="left:436px;top:20px">Blog</a>
      <a style="left:487px;top:20px">Contact Us</a>
    </nav>
    <span class="social-dot" style="left:675px;top:20px;width:12px;height:12px;background:#222"></span>
    <span class="social-dot" style="left:702px;top:20px;width:14px;height:12px;border-radius:4px;background:#e02a2a"></span>
    <div class="abs btn-signin" style="left:731px;top:16px;width:86px;height:22px">Sign In</div>

    <div class="abs hero-line" style="left:38px;top:108px;font-size:48px"><span class="bold">DO</span> <span class="thin">LESS.</span></div>
    <div class="abs hero-line" style="left:38px;top:168px;font-size:48px"><span class="thin">KNOW</span> <span class="bold">MORE.</span></div>
    <div class="abs btn-cta" style="left:40px;top:231px;width:188px;height:30px;font-size:10px;padding:0 3px 0 14px">SIGN UP FOR FREE<span class="arrow" style="width:54px;height:22px"><svg width="26" height="8"><path d="M0 4H24M20 1L24 4L20 7" stroke="#fff" stroke-width="1.3" fill="none"/></svg></span></div>

    <div class="phone" style="left:457px;top:83px;width:105px;height:224px">
      <div class="line" style="left:36px;top:14px;width:30px"></div>
      <div class="line dark" style="left:12px;top:34px;width:60px"></div>
      <div class="line dark" style="left:12px;top:42px;width:30px"></div>
      <div class="toggle" style="left:36px;top:60px"></div>
      <div class="line" style="left:12px;top:90px;width:40px"></div>
      <div class="line" style="left:12px;top:104px;width:30px"></div><div class="toggle" style="left:80px;top:103px"></div>
      <div class="line" style="left:12px;top:120px;width:30px"></div><div class="toggle" style="left:80px;top:119px"></div>
      <div class="line" style="left:12px;top:136px;width:40px"></div><div class="toggle" style="left:80px;top:135px"></div>
      <div class="line" style="left:12px;top:160px;width:50px"></div>
      <div class="line" style="left:12px;top:180px;width:36px"></div><div class="toggle" style="left:80px;top:179px"></div>
      <div class="line" style="left:12px;top:196px;width:20px"></div><div class="toggle" style="left:80px;top:195px"></div>
    </div>
    <div class="phone" style="left:583px;top:83px;width:107px;height:224px">
      <div class="line" style="left:38px;top:14px;width:30px"></div>
      <div class="line dark" style="left:14px;top:34px;width:50px"></div>
      <div class="line" style="left:14px;top:46px;width:76px"></div>
      <div class="line" style="left:14px;top:60px;width:66px"></div>
      <div class="line" style="left:14px;top:90px;width:24px"></div><div class="toggle" style="left:82px;top:89px"></div>
      <div class="line" style="left:14px;top:110px;width:24px"></div><div class="toggle" style="left:82px;top:109px"></div>
      <div class="line" style="left:14px;top:130px;width:24px"></div><div class="toggle" style="left:82px;top:129px"></div>
      <div class="line" style="left:14px;top:150px;width:24px"></div>
      <div class="line" style="left:14px;top:170px;width:24px"></div>
      <div class="line" style="left:14px;top:190px;width:24px"></div>
    </div>
    <div class="phone" style="left:710px;top:83px;width:106px;height:224px">
      <div class="line" style="left:30px;top:14px;width:40px;background:var(--blue)"></div>
      <div class="line" style="left:30px;top:30px;width:44px"></div>
      <div class="line" style="left:12px;top:52px;width:40px;background:var(--blue)"></div>
      <div class="line" style="left:12px;top:66px;width:80px"></div>
      <div class="line" style="left:12px;top:88px;width:80px"></div>
      <div class="abs" style="left:12px;top:100px;width:18px;height:14px;background:#8fd19e"></div>
      <div class="line" style="left:36px;top:104px;width:56px;background:#8fd19e"></div>
      <div class="line" style="left:12px;top:130px;width:40px"></div>
      <div class="line" style="left:12px;top:144px;width:70px"></div>
      <div class="abs" style="left:12px;top:168px;width:16px;height:14px;background:#9aa4ad"></div>
      <div class="line dark" style="left:34px;top:170px;width:56px"></div>
      <div class="line" style="left:12px;top:202px;width:36px;background:var(--blue)"></div>
    </div>

    <div class="art art--network" role="img" aria-label="Illustration of a laptop sending finance emails, charts and reports to many people along dashed lines" style="left:88px;top:386px;width:312px;height:272px"></div>
    <div class="abs brand" style="left:457px;top:470px;font-size:21px"><span class="brand-dot" style="width:11px;height:11px"></span>Coinvale</div>
    <div class="abs lede" style="left:457px;top:508px;font-size:26px">is your free, personalized,</div>
    <div class="abs headline" style="left:457px;top:545px;font-size:28px">Data-Driven Finance Email</div>

    <div class="abs lede" style="left:40px;top:745px;font-size:26px">Stop scanning charts</div>
    <div class="abs headline" style="left:40px;top:781px;font-size:27px">And Chasing Data</div>
    <div class="abs body-copy" style="left:40px;top:829px;font-size:9.5px;width:330px">Don't Bend Over Backwards To Get The Investment Insights You Need. You Have Better Ways To Spend Your Time And Energy.</div>
    <div class="art art--beach" role="img" aria-label="Illustration of a relaxed sloth in a beach chair holding a drink on the shore" style="left:415px;top:660px;width:442px;height:290px;clip-path:polygon(8% 60%,40% 22%,100% 8%,100% 86%,10% 90%,2% 82%)"></div>

    <svg class="abs" style="left:0;top:1050px" width="857" height="320" aria-hidden="true">
      <path d="M0 320 L0 255 L820 60 Q857 52 857 80 V306 Z" fill="var(--blue)"/>
    </svg>
    <div class="art art--photo" role="img" aria-label="Photo of a smiling woman in a red sweater hugging a laptop" style="left:60px;top:921px;width:260px;height:382px;border-radius:45% 45% 0 0 / 30% 30% 0 0"></div>
    <div class="art art--sketch" role="img" aria-label="Line drawing of a sloth in a suit reading a letter" style="left:675px;top:1041px;width:115px;height:245px;border-radius:50px 50px 20px 20px"></div>
    <div class="abs lede" style="left:350px;top:988px;font-size:26px">Let the information</div>
    <div class="abs headline" style="left:350px;top:1026px;font-size:27px">Come Right To You</div>
    <div class="abs body-copy" style="left:350px;top:1072px;font-size:9.5px;width:245px">We'll send you curated market insights exactly when you want them.</div>

    <div class="step" style="left:33px;top:1347px;width:180px">
      <div class="step-badge" style="width:74px;height:74px"><span style="top:18px;width:46px;height:74px;font-size:20px">01</span></div>
      <div class="step-title" style="margin-top:26px;font-size:14px">Your Schedule</div>
      <div class="step-copy" style="margin-top:8px;font-size:9px">Customize When You Get Your Email. Up To Every Half An Hour During Main Exchange Trading Hours.</div>
    </div>
    <div class="step" style="left:338px;top:1347px;width:180px">
      <div class="step-badge" style="width:74px;height:74px"><span style="top:18px;width:46px;height:74px;font-size:20px">02</span></div>
      <div class="step-title" style="margin-top:26px;font-size:14px">Your Assets</div>
      <div class="step-copy" style="margin-top:8px;font-size:9px">Choose From Thousands Of Assets To Include In Your Email. QRTX, LMV, NORA And More!</div>
    </div>
    <div class="step" style="left:641px;top:1347px;width:180px">
      <div class="step-badge" style="width:74px;height:74px"><span style="top:18px;width:46px;height:74px;font-size:20px">03</span></div>
      <div class="step-title" style="margin-top:26px;font-size:14px">All The Data</div>
      <div class="step-copy" style="margin-top:8px;font-size:9px">We Provide As Much Data On Assets As We Can, Including Price, Price Change, Analyst Ratings, Technical Indicators, And News.<br>Want More? Let Us Know!</div>
    </div>

    <div class="art art--field" role="img" aria-label="Illustration of a sloth in a suit chasing floating stock tickers with a butterfly net across grass" style="left:0;top:1611px;width:448px;height:255px;clip-path:polygon(0 62%,55% 28%,88% 34%,100% 62%,96% 92%,88% 100%,0 100%)"></div>
    <div class="abs lede" style="left:483px;top:1677px;font-size:26px">Stop paying</div>
    <div class="abs headline" style="left:483px;top:1712px;font-size:27px">For Information</div>
    <div class="abs body-copy" style="left:483px;top:1757px;font-size:9.5px;width:260px">Don't spend a dime on financial information, use that money for investments</div>
    <div class="abs" style="left:483px;top:1793px;font-size:14px;color:#333">Coinvale Is Free. Period.</div>

    <footer class="footer" style="left:0;top:1894px;width:857px;height:189px">
      <div class="abs brand brand--light" style="left:40px;top:24px;font-size:21px"><span class="brand-dot" style="width:11px;height:11px"></span>Coinvale</div>
      <div class="rule" style="left:40px;top:64px;width:133px"></div>
      <div class="abs tag" style="left:40px;top:76px;font-size:14px"><span class="accent">Do Less,</span> Know More Today</div>
      <div class="abs btn-cta" style="left:40px;top:107px;width:173px;height:29px;font-size:9.5px;padding:0 3px 0 14px;box-shadow:none">SIGN UP FOR FREE<span class="arrow" style="width:50px;height:21px"><svg width="24" height="8"><path d="M0 4H22M18 1L22 4L18 7" stroke="#fff" stroke-width="1.3" fill="none"/></svg></span></div>
      <div class="sample" style="left:40px;top:154px;font-size:9px">See A Full Email Sample</div>
      <div class="art" role="img" aria-label="Line sketch of a sloth in a suit" style="left:275px;top:18px;width:80px;height:160px;border-radius:30px;background:linear-gradient(180deg,#4a4748,#353233)"></div>
      <h4 style="left:471px;top:18px;font-size:14px">Quick Links</h4>
      <div class="links" style="font-size:9px">
        <a style="left:471px;top:52px">About</a>
        <a style="left:471px;top:75px">Blog</a>
        <a style="left:471px;top:98px">Terms Of Use</a>
        <a style="left:471px;top:121px">Privacy Policy</a>
      </div>
      <h4 style="left:675px;top:18px;font-size:14px">Social Links</h4>
      <span class="social-dot" style="left:677px;top:58px;width:20px;height:20px;background:var(--blue)"></span>
      <span class="social-dot" style="left:709px;top:58px;width:20px;height:20px;background:var(--blue)"></span>
      <div class="abs" style="left:702px;top:160px;font-size:8.5px">Copyright © 2023 Coinvale LLC</div>
    </footer>
  </main>

  <!-- MOBILE -->
  <main class="page page--mobile">
    <svg class="abs" style="left:0;top:0" width="215" height="330" aria-hidden="true">
      <defs>
        <linearGradient id="heroFadeM" x1="0" y1="0" x2="0" y2="1">
          <stop offset="0" stop-color="#ffffff"/>
          <stop offset="0.15" stop-color="#e6f2fb"/>
          <stop offset="0.5" stop-color="#0a7bd0"/>
          <stop offset="1" stop-color="#0a7bd0"/>
        </linearGradient>
      </defs>
      <path d="M0 0 H215 V120 L40 250 Q12 275 0 330 Z" fill="url(#heroFadeM)"/>
    </svg>
    <div class="abs brand" style="left:10px;top:9px;font-size:16px;gap:5px"><span class="brand-dot" style="width:8px;height:8px"></span>Coinvale</div>
    <svg class="abs" style="left:184px;top:12px" width="20" height="16" aria-hidden="true"><path d="M0 1H20M6 8H20M0 15H20" stroke="var(--blue)" stroke-width="1.3"/></svg>
    <div class="abs hero-line" style="left:7px;top:72px;font-size:28px"><span class="bold">DO</span> <span class="thin">LESS.</span></div>
    <div class="abs hero-line" style="left:7px;top:107px;font-size:28px"><span class="thin">KNOW</span> <span class="bold">MORE.</span></div>
    <div class="abs btn-cta" style="left:7px;top:150px;width:141px;height:25px;font-size:8px;padding:0 3px 0 9px">SIGN UP FOR FREE<span class="arrow" style="width:38px;height:18px"><svg width="20" height="8"><path d="M0 4H18M14 1L18 4L14 7" stroke="#fff" stroke-width="1.2" fill="none"/></svg></span></div>
    <div class="phone" style="left:16px;top:199px;width:55px;height:114px;border-width:2px;border-radius:8px">
      <div class="line dark" style="left:6px;top:14px;width:30px;height:2px"></div>
      <div class="line" style="left:6px;top:34px;width:38px;height:2px"></div>
      <div class="line" style="left:6px;top:54px;width:38px;height:2px"></div>
      <div class="line" style="left:6px;top:74px;width:38px;height:2px"></div>
    </div>
    <div class="phone" style="left:79px;top:199px;width:55px;height:114px;border-width:2px;border-radius:8px">
      <div class="line dark" style="left:6px;top:14px;width:26px;height:2px"></div>
      <div class="line" style="left:6px;top:34px;width:38px;height:2px"></div>
      <div class="line" style="left:6px;top:54px;width:38px;height:2px"></div>
      <div class="line" style="left:6px;top:74px;width:38px;height:2px"></div>
    </div>
    <div class="phone" style="left:142px;top:199px;width:55px;height:114px;border-width:2px;border-radius:8px">
      <div class="line" style="left:6px;top:14px;width:26px;height:2px;background:var(--blue)"></div>
      <div class="line" style="left:6px;top:34px;width:38px;height:2px"></div>
      <div class="line" style="left:6px;top:54px;width:38px;height:2px"></div>
      <div class="line" style="left:6px;top:74px;width:38px;height:2px"></div>
    </div>

    <div class="abs brand" style="left:9px;top:350px;font-size:17px;gap:5px"><span class="brand-dot" style="width:9px;height:9px"></span>Coinvale</div>
    <div class="abs lede" style="left:9px;top:381px;font-size:14px">is your free, personalized,</div>
    <div class="abs headline" style="left:9px;top:403px;font-size:14.5px">Data-Driven Finance Email</div>
    <div class="art art--network" role="img" aria-label="Illustration of a laptop sending finance emails to many people" style="left:22px;top:443px;width:172px;height:152px"></div>
    <div class="abs" style="left:0;top:631px;width:215px;height:1px;background:#dde3e8"></div>

    <div class="abs lede" style="left:6px;top:646px;font-size:14px">Stop scanning charts</div>
    <div class="abs headline" style="left:6px;top:667px;font-size:14px">And Chasing Data</div>
    <div class="abs body-copy" style="left:8px;top:691px;font-size:9px;width:195px">Don't Bend Over Backwards To Get The Investment Insights You Need. You Have Better Ways To Spend Your Time And Energy.</div>
    <div class="art art--beach" role="img" aria-label="Illustration of a relaxed sloth in a beach chair holding a drink" style="left:0;top:761px;width:215px;height:230px;clip-path:polygon(0 48%,55% 18%,100% 8%,100% 68%,0 78%)"></div>

    <div class="abs lede" style="left:10px;top:977px;font-size:14px">Let the information</div>
    <div class="abs headline" style="left:10px;top:998px;font-size:14px">Come Right To You</div>
    <div class="abs body-copy" style="left:10px;top:1021px;font-size:9px;width:190px">We'll send you curated market insights exactly when you want them.</div>
    <svg class="abs" style="left:0;top:1110px" width="215" height="177" aria-hidden="true"><path d="M0 177 V150 L200 10 Q215 0 215 20 V177 Z" fill="var(--blue)"/></svg>
    <div class="art art--photo" role="img" aria-label="Photo of a smiling woman in a red sweater hugging a laptop" style="left:12px;top:1075px;width:150px;height:210px;border-radius:45% 45% 0 0 / 30% 30% 0 0"></div>
    <div class="art art--sketch" role="img" aria-label="Line drawing of a sloth in a suit reading a letter" style="left:168px;top:1140px;width:44px;height:140px;border-radius:22px"></div>

    <div class="step" style="left:15px;top:1320px;width:185px">
      <div class="step-badge" style="width:74px;height:74px"><span style="top:14px;width:44px;height:74px;font-size:19px">01</span></div>
      <div class="step-title" style="margin-top:22px;font-size:13.5px">Your Schedule</div>
      <div class="step-copy" style="margin-top:6px;font-size:9px">Customize When You Get Your Email. Up To Every Half An Hour During Main Exchange Trading Hours.</div>
    </div>
    <div class="step" style="left:15px;top:1525px;width:185px">
      <div class="step-badge" style="width:74px;height:74px"><span style="top:14px;width:44px;height:74px;font-size:19px">02</span></div>
      <div class="step-title" style="margin-top:22px;font-size:13.5px">Your Assets</div>
      <div class="step-copy" style="margin-top:6px;font-size:9px">Choose From Thousands Of Assets To Include In Your Email. QRTX, LMV, NORA And More!</div>
    </div>
    <div class="step" style="left:15px;top:1728px;width:185px">
      <div class="step-badge" style="width:74px;height:74px"><span style="top:14px;width:44px;height:74px;font-size:19px">03</span></div>
      <div class="step-title" style="margin-top:22px;font-size:13.5px">All The Data</div>
      <div class="step-copy" style="margin-top:6px;font-size:9px">We Provide As Much Data On Assets As We Can, Including Price, Price Change, Analyst Ratings, Technical Indicators, And News.<br>Want More? Let Us Know!</div>
    </div>

    <div class="abs lede" style="left:9px;top:1946px;font-size:14px">Stop paying</div>
    <div class="abs headline" style="left:9px;top:1967px;font-size:14px">For Information</div>
    <div class="abs body-copy" style="left:9px;top:1992px;font-size:9px;width:160px">Don't spend a dime on financial information, use that money for investments</div>
    <div class="abs" style="left:9px;top:2038px;font-size:11.5px;color:#333">Coinvale Is Free. Period.</div>
    <div class="art art--field" role="img" aria-label="Illustration of a sloth chasing stock tickers with a butterfly net" style="left:0;top:2085px;width:215px;height:152px;clip-path:polygon(0 55%,50% 28%,100% 30%,100% 100%,0 100%)"></div>

    <footer class="footer" style="left:0;top:2237px;width:215px;height:359px">
      <div class="art" role="img" aria-label="Line sketch of a sloth in a suit" style="left:72px;top:200px;width:44px;height:130px;border-radius:22px;background:linear-gradient(180deg,#4a4748,#353233)"></div>
      <div class="abs brand brand--light" style="left:10px;top:38px;font-size:19px;gap:6px"><span class="brand-dot" style="width:10px;height:10px"></span>Coinvale</div>
      <div class="rule" style="left:10px;top:80px;width:165px"></div>
      <div class="abs tag" style="left:11px;top:89px;font-size:13px"><span class="accent">Do Less,</span> Know More Today</div>
      <div class="abs btn-cta" style="left:11px;top:120px;width:174px;height:29px;font-size:9px;padding:0 3px 0 12px;box-shadow:none">SIGN UP FOR FREE<span class="arrow" style="width:48px;height:21px"><svg width="24" height="8"><path d="M0 4H22M18 1L22 4L18 7" stroke="#fff" stroke-width="1.3" fill="none"/></svg></span></div>
      <div class="sample" style="left:11px;top:163px;font-size:8.5px">See A Full Email Sample</div>
      <h4 style="left:6px;top:186px;font-size:13.5px">Quick Links</h4>
      <h4 style="left:123px;top:186px;font-size:13.5px">Social Links</h4>
      <div class="links" style="font-size:9px">
        <a style="left:7px;top:222px">About</a>
        <a style="left:7px;top:245px">Blog</a>
        <a style="left:7px;top:268px">Terms Of Use</a>
        <a style="left:7px;top:291px">Privacy Policy</a>
      </div>
      <span class="social-dot" style="left:126px;top:225px;width:19px;height:19px;background:var(--blue)"></span>
      <span class="social-dot" style="left:158px;top:225px;width:19px;height:19px;background:var(--blue)"></span>
      <div class="abs" style="left:0;top:335px;width:215px;text-align:center;font-size:8px">Copyright © 2023 Coinvale LLC</div>
    </footer>
  </main>
</div>
</body>
</html>
```